Park furniture company needs a new product flyer

We're a street and park furniture supply company and we have a new range of furniture that we would like to showcase to prospective customers.
Pictures, logo and copy attached.
Furniture pictures are also available with a black background.
Warranty information needs to feature on the flyer.
Recycled content information needs to feature on the flyer.

Target Market(s)

Landscape Architects

Font styles to use
Serif

Requirements
Must have
• Professional fonts and graphics.
Should not have
• comic sans or similar fonts - cheap graphics

```html
<!DOCTYPE html>
<html lang="en">
<head>
<meta charset="utf-8">
<title>Laneway Commons – Product Flyer</title>
<link href="https://fonts.googleapis.com/css2?family=Montserrat:wght@300;400;600;700&display=swap" rel="stylesheet">
<style>
  :root {
    --brand-blue: #0a75bc;
    --charcoal: #555655;
    --logo-grey: #58585a;
    --white: #ffffff;
    --paper: #ffffff;
    --frame-light: #e6e1d6;
    --timber-dark: #4a4038;
    --timber-warm: #a5521f;
  }
  * { margin: 0; padding: 0; box-sizing: border-box; }
  html, body { width: 849px; height: 1200px; overflow: hidden; background: var(--paper); }
  .flyer {
    position: relative;
    width: 849px;
    height: 1200px;
    background: var(--paper);
    font-family: "Montserrat", sans-serif;
    color: var(--white);
  }

  /* Brand name */
  .brand {
    position: absolute;
    right: 56px;
    top: 36px;
    text-align: right;
    color: var(--logo-grey);
    font-weight: 700;
    line-height: 1;
  }
  .brand-main { display: block; font-size: 56px; letter-spacing: -1px; }
  .brand-sub { display: block; font-size: 30px; margin-top: 6px; letter-spacing: 0; }

  /* Product photography slots */
  .product-photo {
    position: absolute;
    border-radius: 2px;
  }
  .photo-table-set {
    left: 58px; top: 50px; width: 330px; height: 256px;
    background: linear-gradient(160deg, var(--timber-dark) 0%, #7a6e62 55%, var(--frame-light) 100%);
  }
  .photo-table-front {
    left: 62px; top: 328px; width: 346px; height: 112px;
    background: linear-gradient(180deg, var(--timber-dark) 0%, #8d8275 45%, var(--frame-light) 100%);
  }
  .photo-seat-angle {
    left: 132px; top: 454px; width: 188px; height: 240px;
    background: linear-gradient(150deg, #c08040 0%, var(--timber-warm) 50%, #6e5a46 100%);
  }
  .photo-seat-front {
    left: 76px; top: 716px; width: 312px; height: 152px;
    background: linear-gradient(180deg, var(--timber-warm) 0%, #b8682c 55%, var(--frame-light) 100%);
  }

  /* Copy panel */
  .copy-panel {
    position: absolute;
    left: 417px; top: 161px;
    width: 376px; height: 720px;
    background: var(--brand-blue);
  }
  .copy-intro {
    position: absolute;
    left: 28px; top: 184px;
    top: 23px;
    font-size: 18px;
    font-weight: 600;
    line-height: 29.5px;
    letter-spacing: 0.5px;
  }
  .copy-block {
    position: absolute;
    left: 28px;
    font-size: 13.6px;
    font-weight: 400;
    line-height: 21px;
    letter-spacing: 0.35px;
    white-space: nowrap;
  }
  .copy-block strong { font-weight: 700; }
  .copy-range { top: 156px; }
  .copy-recycled { top: 240px; }
  .copy-warranty { top: 346px; }
  .copy-health { top: 451px; }
  .copy-options { top: 514px; }
  .copy-length { top: 619px; }
  .copy-install { top: 681px; }

  /* Information band */
  .info-band {
    position: absolute;
    left: 40px; top: 880px;
    width: 753px; height: 183px;
    background: var(--charcoal);
    display: flex;
  }
  .info-column {
    flex: 1;
    text-align: center;
    padding-top: 13px;
  }
  .info-column:last-child { padding-left: 8px; }
  .info-title {
    font-size: 14.4px;
    font-weight: 700;
    letter-spacing: 1.3px;
  }
  .info-body {
    margin-top: 20px;
    font-size: 14.4px;
    font-weight: 300;
    line-height: 21.5px;
    letter-spacing: 1px;
  }

  /* Footer */
  .footer-contact {
    position: absolute;
    left: 40px; top: 1062px;
    width: 377px; height: 76px;
    display: flex; align-items: center; justify-content: center;
    color: var(--charcoal);
    font-size: 14.4px; font-weight: 700; letter-spacing: 1.3px;
  }
  .footer-web {
    position: absolute;
    left: 417px; top: 1062px;
    width: 376px; height: 76px;
    background: var(--brand-blue);
    display: flex; align-items: center; justify-content: center;
    padding-right: 20px;
    font-size: 14.4px; font-weight: 700; letter-spacing: 1.3px;
  }
</style>
</head>
<body>
<main class="flyer">
  <div class="brand">
    <span class="brand-main">LANEWAY</span>
    <span class="brand-sub">Commons</span>
  </div>

  <div class="product-photo photo-table-set" role="img" aria-label="Picnic table with two bench seats, composite timber battens on a light aluminium frame"></div>
  <div class="product-photo photo-table-front" role="img" aria-label="Front view of the table and bench set"></div>
  <div class="product-photo photo-seat-angle" role="img" aria-label="Angled view of a seat with backrest and armrests in warm timber-look battens"></div>
  <div class="product-photo photo-seat-front" role="img" aria-label="Front view of the seat with backrest and armrests"></div>

  <section class="copy-panel">
    <h1 class="copy-intro">European inspired with a unique<br>and original design, that is<br>functional all while respecting<br>the environment.</h1>
    <p class="copy-block copy-range">Our range is designed to make life easier<br>for people; created using extremely<br>durable, ultra low maintenance materials.</p>
    <p class="copy-block copy-recycled">Featuring <strong>98% recycled</strong> composite<br>battens in a range of stain and fade-<br>resistant colour options and a unique<br>aluminium frame design.</p>
    <p class="copy-block copy-warranty">The capped composite battens come<br>with a <strong>10-year commercial warranty</strong><br>covering staining, fading and structural<br>performance.</p>
    <p class="copy-block copy-health">Site-specific for healthcare applications<br>offering wheelchair accessibility options</p>
    <p class="copy-block copy-options">The Laneway Commons range comprises<br>of a seat with optional armrests, bench<br>seat and table, available in both standard<br>or DDA designs.</p>
    <p class="copy-block copy-length">Uniform length of 1800mm with tailored<br>options available.</p>
    <p class="copy-block copy-install">Bolt down or freestanding options.</p>
  </section>

  <section class="info-band">
    <div class="info-column">
      <h2 class="info-title">RECYCLED CONTENT INFORMATION</h2>
      <p class="info-body">TEXT TO BE SUPPLIED -COULD<br>INCLUDE CUSTOM&nbsp; RECYCLE ICON</p>
    </div>
    <div class="info-column">
      <h2 class="info-title">10 YEAR WARRANTY INFORMATION</h2>
      <p class="info-body">TEXT TO BE SUPPLIED -COULD<br>INCLUDE WARRANTY ICON</p>
    </div>
  </section>

  <footer>
    <div class="footer-contact">CONTACT INFORMATION GOES HERE</div>
    <div class="footer-web">WEBSITE URL GOES HERE</div>
  </footer>
</main>
</body>
</html>
```